Banner Ad for website hompage - Design Project

We need 4 banner ads for the homepage of a Rent a Car company based in dubai. We rent a wide range of cars but mainly deal in the affordable cars category. Our website colors are mainly red, white and black and I can send pictures of the website (attached) if you want something to compare possible design ideas with. The banners need to promote different messages and must be appealing to the end user. It must also use pictures of cars that exist in our fleet (Pls note: this is only if you are using cars in the banner ad)

The 4 banner ads needed are as follows:
1) should promote something along the lines of we have 20+ models available and reserve a car now (This banner should also have a reserve now button, not the actual button but it's design. The button will be made and coded by us)
2) should promote something along the lines of we offer personalised service and we look after each and every custoemr individually
3) we provide attractive rates based on daily, weekly, monthly and longer rental periods (should also incorporate a reserve now message)
4) Like us on bramblex and follow us on social media for additional offers and discounts (would like for this to have a like button design implemented in it which will be linked to bramblex.)

Also please not the picture file size is 940pixels by 400pixels

Finally: I also need the psd files for the banners.

Reason: giving people more time for revisions

It Company

```html
<!DOCTYPE html>
<html lang="en">
<head>
<meta charset="utf-8">
<title>Rental Banners</title>
<link rel="stylesheet" href="https://fonts.googleapis.com/css2?family=Roboto:wght@700;900&display=swap">
<style>
  :root {
    --brand-red: #e0101b;
    --brand-red-dark: #b0070f;
    --ink-grey: #58595b;
    --panel-top: #ffffff;
    --panel-bottom: #e4e4e4;
    --page: #ffffff;
  }
  html, body {
    margin: 0;
    padding: 0;
    width: 1200px;
    height: 1070px;
    overflow: hidden;
    background: var(--page);
  }
  .canvas {
    position: relative;
    width: 1200px;
    height: 1070px;
  }
  .banner {
    position: absolute;
    left: 17px;
    width: 1168px;
    height: 501px;
  }
  .banner--fleet { top: 12px; }
  .banner--service { top: 552px; }
  .banner svg { display: block; }
  .headline {
    font-family: "Roboto", Arial, sans-serif;
    font-weight: 900;
  }
  .headline--red { fill: var(--brand-red); }
  .headline--grey { fill: var(--ink-grey); }
  .button-label {
    font-family: "Roboto", Arial, sans-serif;
    font-weight: 700;
    fill: #ffffff;
  }
</style>
</head>
<body>
<main class="canvas">

  <section class="banner banner--fleet">
    <svg width="1168" height="501" viewBox="0 0 1168 501">
      <defs>
        <linearGradient id="panelFade" x1="0" y1="0" x2="0" y2="1">
          <stop offset="0" stop-color="var(--panel-top)"/>
          <stop offset="1" stop-color="var(--panel-bottom)"/>
        </linearGradient>
        <linearGradient id="carTones" x1="0" y1="0" x2="1" y2="1">
          <stop offset="0" stop-color="#d9dadc"/>
          <stop offset="0.55" stop-color="#8e9093"/>
          <stop offset="1" stop-color="#f2f2f2"/>
        </linearGradient>
        <linearGradient id="buttonRed" x1="0" y1="0" x2="0" y2="1">
          <stop offset="0" stop-color="var(--brand-red)"/>
          <stop offset="1" stop-color="var(--brand-red-dark)"/>
        </linearGradient>
      </defs>
      <rect class="panel" x="0" y="0" width="1168" height="501" fill="url(#panelFade)"/>
      <polygon class="photo" role="img" aria-label="Silver SUV from the rental fleet, low front three-quarter view"
               points="0,0 583,0 521,501 0,501" fill="url(#carTones)"/>
      <polygon class="divider" points="583,0 610,0 548,501 521,501" fill="var(--brand-red)"/>
      <text class="headline headline--red" x="899" y="186" font-size="200" text-anchor="middle"
            textLength="335" lengthAdjust="spacingAndGlyphs">20+</text>
      <text class="headline headline--grey" x="899" y="263" font-size="84" text-anchor="middle"
            textLength="335" lengthAdjust="spacingAndGlyphs">MODELS</text>
      <text class="headline headline--grey" x="899" y="325" font-size="73" text-anchor="middle"
            textLength="338" lengthAdjust="spacingAndGlyphs">AVAILABLE</text>
      <g class="reserve-button">
        <polygon points="700,402 724,394 676,471 652,471" fill="#f4f4f4"/>
        <polygon points="724,394 1100,394 1100,471 676,471" fill="url(#buttonRed)"/>
        <text class="button-label" x="912" y="449" font-size="45" text-anchor="middle"
              textLength="316" lengthAdjust="spacingAndGlyphs">RESERVE NOW</text>
      </g>
    </svg>
  </section>

  <section class="banner banner--service">
    <svg width="1168" height="502" viewBox="0 0 1168 502">
      <defs>
        <linearGradient id="panelFade2" x1="0" y1="0" x2="0" y2="1">
          <stop offset="0" stop-color="var(--panel-top)"/>
          <stop offset="1" stop-color="var(--panel-bottom)"/>
        </linearGradient>
        <linearGradient id="familyTones" x1="0" y1="0" x2="1" y2="1">
          <stop offset="0" stop-color="#c9c3bd"/>
          <stop offset="0.5" stop-color="#b88c74"/>
          <stop offset="1" stop-color="#5a7fa6"/>
        </linearGradient>
      </defs>
      <rect class="panel" x="0" y="0" width="1168" height="502" fill="url(#panelFade2)"/>
      <polygon class="photo" role="img" aria-label="Smiling family holding up car keys in a showroom"
               points="0,0 583,0 521,502 0,502" fill="url(#familyTones)"/>
      <polygon class="divider" points="583,0 610,0 548,502 521,502" fill="var(--brand-red)"/>
      <text class="headline headline--red" x="888" y="208" font-size="58" text-anchor="middle"
            textLength="443" lengthAdjust="spacingAndGlyphs">PERSONALISED</text>
      <text class="headline headline--grey" x="888" y="302" font-size="105" text-anchor="middle"
            textLength="437" lengthAdjust="spacingAndGlyphs">SERVICE</text>
    </svg>
  </section>

</main>
</body>
</html>
```